Looking for a modern, Professional business card design

We have a simple business card, but are looking for a more modern, professional look. A sample of the basic card is attached as well as the logo. We would also like to add that we offer:
Struggling with your finances?
- Learn to become debt free
- Discover the power of cash
- Control your money instead of it controlling you
Let us help you achieve a new level of financial freedom!
Also, we would like to have a "SPECIAL OFFER!: FREE 30 minute consultation"
Financial Planning

```html
<!DOCTYPE html>
<html lang="en">
<head>
<meta charset="utf-8">
<title>SteadyPath Money Coaching – Business Card</title>
<link href="https://fonts.googleapis.com/css2?family=Open+Sans:ital,wght@0,400;0,600;0,700;0,800;1,400;1,600&display=swap" rel="stylesheet">
<style>
  :root {
    --green-deep: #2f8a2a;
    --green-mid: #4faa2e;
    --green-light: #a8d43c;
    --green-brand: #3d9a2c;
    --ink: #1b1b1b;
    --grey-text: #555a5e;
    --white: #ffffff;
    --backdrop: #e9e6df;
  }
  * { box-sizing: border-box; margin: 0; padding: 0; }
  html, body {
    width: 1200px; height: 843px; overflow: hidden;
    background: var(--backdrop);
    font-family: "Open Sans", Arial, sans-serif;
  }
  .canvas {
    width: 1200px; height: 843px;
    display: flex; flex-direction: column; align-items: center; justify-content: center;
    gap: 40px;
  }
  .card {
    position: relative;
    width: 660px; height: 377px;
    border-radius: 22px;
    overflow: hidden;
    box-shadow: 0 6px 18px rgba(0,0,0,.18);
  }

  /* ---------- Back side ---------- */
  .card-back {
    background: radial-gradient(ellipse at 72% 40%, var(--green-light) 0%, var(--green-mid) 45%, var(--green-deep) 100%);
    color: var(--white);
    padding: 34px 40px;
  }
  .offer-heading { font-weight: 700; font-size: 21px; letter-spacing: .3px; }
  .benefits { list-style: none; margin-top: 4px; }
  .benefits li {
    font-style: italic; font-size: 17px; line-height: 1.35;
    padding-left: 20px; position: relative;
  }
  .benefits li::before {
    content: ""; position: absolute; left: 2px; top: 9px;
    width: 8px; height: 8px; border-radius: 50%; background: var(--white);
  }
  .invite { font-style: italic; font-size: 17px; margin-top: 8px; }
  .special { font-weight: 800; font-size: 24px; margin-top: 16px; line-height: 1.1; }
  .special-detail { font-weight: 600; font-size: 16px; }
  .back-brand {
    margin-top: 18px;
    font-weight: 800; font-size: 30px; line-height: 1; letter-spacing: .5px;
    white-space: nowrap;
    color: var(--white);
  }
  .back-tagline { font-style: italic; font-size: 13px; opacity: .9; margin-top: 6px; }

  /* ---------- Front side ---------- */
  .card-front { background: var(--white); }
  .front-logo {
    position: absolute; left: 90px; top: 44px;
    display: flex; align-items: center; gap: 14px;
  }
  .logo-dot { width: 46px; height: 46px; border-radius: 50%; background: var(--green-brand); flex: none; }
  .logo-text { display: flex; flex-direction: column; }
  .brand-name {
    font-weight: 800; font-size: 24px; color: var(--green-brand);
    letter-spacing: .3px; line-height: 1.1; white-space: nowrap;
  }
  .front-tagline {
    font-style: italic; font-size: 12px; color: var(--grey-text);
    margin-top: 6px; text-align: right;
  }
  .name-band {
    position: absolute; left: 0; top: 138px; width: 560px; height: 88px;
    background: linear-gradient(90deg, var(--green-mid) 0%, var(--green-light) 55%, rgba(255,255,255,0) 100%);
    padding: 12px 0 0 72px; color: var(--white);
  }
  .person-name { font-weight: 600; font-size: 26px; line-height: 1.1; }
  .person-title { font-size: 19px; }
  .band-end {
    position: absolute; right: 0; top: 186px; width: 120px; height: 62px; background: var(--ink);
  }
  .band-mark {
    position: absolute; right: 140px; top: 180px;
    width: 54px; height: 54px; border-radius: 50%; background: var(--green-brand);
  }
  .contact-list {
    position: absolute; left: 42px; top: 252px;
    list-style: none; color: var(--grey-text); font-size: 18px; line-height: 1.45;
  }
  .contact-list li { display: flex; align-items: center; gap: 12px; }
  .contact-list svg { width: 18px; height: 18px; flex: none; }
</style>
</head>
<body>
<main class="canvas">

  <section class="card card-back" aria-label="Card back">
    <h2 class="offer-heading">STRUGGLING WITH YOUR FINANCES?</h2>
    <ul class="benefits">
      <li>Learn to become debt free</li>
      <li>Discover the power of cash</li>
      <li>Control your money instead of it controlling you</li>
    </ul>
    <p class="invite">Let us help you achieve a new level of financial freedom!</p>
    <p class="special">SPECIAL OFFER!</p>
    <p class="special-detail">FREE 30 minute consultation</p>
    <p class="back-brand">STEADYPATH MONEY COACHING</p>
    <p class="back-tagline">Achieve a new level of personal freedom</p>
  </section>

  <section class="card card-front" aria-label="Card front">
    <div class="front-logo">
      <span class="logo-dot"></span>
      <div class="logo-text">
        <span class="brand-name">STEADYPATH MONEY COACHING</span>
        <p class="front-tagline">Achieve a new level of personal freedom</p>
      </div>
    </div>

    <div class="name-band">
      <p class="person-name">Daniel R. Hayes</p>
      <p class="person-title">Personal Financial Coach</p>
    </div>
    <span class="band-end"></span>
    <span class="band-mark"></span>

    <ul class="contact-list">
      <li>
        <svg viewBox="0 0 18 18" aria-hidden="true"><rect x="5" y="1" width="8" height="16" rx="1.5" fill="none" stroke="#3d9a2c" stroke-width="1.6"/><circle cx="9" cy="14" r="1" fill="#3d9a2c"/></svg>
        (205) 555-0178
      </li>
      <li>
        <svg viewBox="0 0 18 18" aria-hidden="true"><rect x="1.5" y="4" width="15" height="10" fill="#3d9a2c"/><path d="M1.5 4 L9 10 L16.5 4" fill="none" stroke="#fff" stroke-width="1.3"/></svg>
        daniel@steadypathmoney.com
      </li>
      <li>
        <svg viewBox="0 0 18 18" aria-hidden="true"><circle cx="9" cy="9" r="7.5" fill="#3d9a2c"/><ellipse cx="9" cy="9" rx="3.2" ry="7.5" fill="none" stroke="#fff" stroke-width="1.1"/><line x1="1.5" y1="9" x2="16.5" y2="9" stroke="#fff" stroke-width="1.1"/></svg>
        www.steadypathmoney.com
      </li>
    </ul>
  </section>

</main>
</body>
</html>
```